Brisk Open Panel – Project specifications

Introduction:

Brisk Open Panel (BOP) is an android screen unlock app allowing users to unlock their screen by opening one of their most used apps and so save the need to go to phone home screen and search for that app in order to open it.

Upon installation of the app end user will be presented with a screen that includes an End User License Agreement which the user will be able to Accept or Decline. Upon Acceptance user will be presented with a screen that includes a textual description of the app and an option to choose between a grid view and a list view and also to enable or disable the app. Once the user clicks Enable the app will close and the BOP functionality will start operating for the user. If the user hits Disable there will be another screen presented asking to user to confirm app disabling.

BOP Functionalities:

BOP Interface:
• The interface of BOP will be presented to users every time they wish to "wake-up" their device from lock scree state (typically by clicking home button or one of the side buttons of the device).
• BOP will allow user to unlock screen by selecting one of the apps installed on his/her device. Such selection will unlock the screen and open the selected app at the same time.
• BOP user interface will be presented as one of the followings:

(1) List View - a wall of stripes, each stripe will display an icon of a frequent or recent used app (following logic described below) and swiping such stripe from left to right or from right to left will unlock the screen and at the same time open the selected app so that user will be able to use the selected app immediately upon unlocking the screen.

or

(2) Grid View - a grid of apps following the same logic where each of the app icons can be tapped and dragged to open that app

List view screen:

• The BOP will present the Top 10 used apps in a form of stripes that are framed in the unlock screen. Each stripe will include an icon of the app in the middle of the stripe.
• User will be able to scroll up and down through the unlock screen without unlocking it
• User will be able to unlock screen by swiping the icon from left to right or from right to left and the design should hint that option. Doing this will unlock the screen and will open the app
• Two additional stripes - Stripe number four and the stripe before the last one will present an icon of an advertisement and these stripe will look slightl differently from other stripes.
The very last stripe will be a "Powered By Brisk Open" stripe and swiping this stripe will open the Brisk Open app. It should also look a little different from the others
• In case user has an unread text message or a missed call there will be an icon to indicate that and each of the icons will be presented as the first and second stripe from the top
• In addition - the very first stripe will have an unlock icon and it will also look a little different from app stripes as to indicate that swiping that stripe will just unlock the screen without opening a specific app
• At the bottom of the screen there will be a disabled button which will be activated by sliding that button upwards (and the design should indicate that). Once slides upwards it will open a screen with the text: "Are you sure you want to disable Brisk Open Panel?" and it will have two buttons for yes and no.

SEE SAMPLE PLACEHOLDERS SCREENS FOR LIST VIEW ATTACHED TO PROJECT OVERVIEW

Grid View Screen:

• The BOP grid view screen will show a grid of 9 icons each (three icons in a raw) The middle icon in this grid will be an ad icon and it will look slightly different
• Below the grid there will be a stripe with unlock icon in the middle to indicate that swiping this stripe will unlock the screen without opening a specific app
• Below the strip there will be two rectangular banners - one can be swiped to the left and the other can be swiped to the right and they will be reserved for an ad icons and Powerd By icon that row will look a little different

SEE SAMPLE PLACEHOLDERS SCREENS FOR GRID VIEW ATTACHED TO PROJECT OVERVIEW

Graphic material needed:

• App icon indicating this is a Brisk Open Panel App
• User agreement screen
• App description screen with ability to choose between list view and grid view + disable and enable
• List view screen (scrollable up and down - so this is a long screen)
• Grid view screen
• Disable confirmation screen

Attached sample screenshots. Hope this is clear....

```html
<!DOCTYPE html>
<html lang="en">
<head>
<meta charset="UTF-8">
<title>User Agreement – Brisk Open Panel</title>
<link rel="stylesheet" href="https://fonts.googleapis.com/css2?family=Arimo:wght@400;700&display=swap">
<style>
  :root {
    --header-blue: #003f8f;
    --bg-center: #78f2f6;
    --bg-mid: #12a9d6;
    --bg-edge: #0050a6;
    --panel-fill: rgba(205, 225, 240, 0.55);
    --text-dark: #231f20;
    --white: #ffffff;
    --silver-light: #f4f4f4;
    --silver-mid: #c9c9cb;
    --silver-dark: #a9a9ad;
  }
  * { box-sizing: border-box; margin: 0; padding: 0; }
  html, body {
    width: 729px;
    height: 1200px;
    overflow: hidden;
  }
  body {
    font-family: "Arimo", Arial, sans-serif;
    color: var(--text-dark);
  }
  .screen {
    position: relative;
    width: 729px;
    height: 1200px;
    overflow: hidden;
    background: radial-gradient(ellipse 520px 720px at 364px 560px,
      var(--bg-center) 0%, var(--bg-mid) 55%, var(--bg-edge) 100%);
  }
  .screen-header {
    position: absolute;
    left: 0; top: 0;
    width: 100%;
    height: 88px;
    background: var(--header-blue);
    display: flex;
    align-items: center;
    justify-content: center;
  }
  .screen-title {
    color: var(--white);
    font-weight: 700;
    font-size: 33px;
    letter-spacing: 0.2px;
  }
  .agreement-panel {
    position: absolute;
    left: 51px;
    top: 127px;
    width: 626px;
    height: 852px;
    border-radius: 24px;
    background: var(--panel-fill);
  }
  .agreement-text {
    position: absolute;
    left: 29px;
    top: 28px;
    width: 567px;
    height: 752px;
    overflow: hidden;
    font-size: 27.5px;
    line-height: 35.7px;
    text-align: justify;
  }
  .agreement-text p + p { margin-top: 35.7px; }
  .agreement-text p.joined { margin-top: 0; }
  .ok-button {
    position: absolute;
    left: 189px;
    top: 1009px;
    width: 344px;
    height: 84px;
    border-radius: 10px;
    border: 3px solid #e6e6e8;
    background: linear-gradient(100deg,
      var(--silver-dark) 0%, var(--silver-light) 28%, var(--silver-mid) 50%,
      var(--silver-light) 72%, var(--silver-dark) 100%);
    box-shadow: inset 0 0 0 2px rgba(150,150,155,0.6);
    font-family: inherit;
    font-weight: 700;
    font-size: 36px;
    color: var(--text-dark);
    display: flex;
    align-items: center;
    justify-content: center;
  }
</style>
</head>
<body>
  <main class="screen">
    <header class="screen-header">
      <h1 class="screen-title">User Agreement</h1>
    </header>

    <section class="agreement-panel">
      <div class="agreement-text">
        <p>At the bottom of the screen there will be a disabled button which will be activated by sliding that button upwards (and the design should indicate that). Once slides upwards it will open a screen with the text: "Are you sure you want to disable Brisk Open Panel?" and it will have two buttons for yes and no.</p>
        <p>At the bottom of the screen there will be a disabled button which will be activated by sliding that button upwards (and the design should indicate that). Once slides upwards it will open a screen with the text: "Are you sure you want to disable Brisk Open Panel?" and it will have two buttons for yes and no.</p>
        <p class="joined">At the bottom of the screen there will be a disabled button which will be activated by sliding that button upwards (and the design should indicate that). Once slides upwards it will open a screen with the text: "Are you sure you want to disable Brisk Open Panel?" and it will have two buttons for yes and no.</p>
      </div>
    </section>

    <button class="ok-button" type="button">OK</button>
  </main>
</body>
</html>
```